Business Card Design Project

Require a business card for a swing band called "Velvet Brass Parade". We are a 6 piece band that performs at events and corporate functions. Our music is great for dancing to or just providing a classy background atmosphere for people to enjoy. Final design should communicate professionalism and style with a hint of fun.

Sorry, just realised that it needs to be single sided only. Also, no rounded edges.

Industry/Entity Type

Events

Requirements
Must have
• Contact number: 0438 216 903
email address: velvetbrassparade@mailbox-demo.net
Website details: www.velvetbrassparade-demo.com

```html
<!DOCTYPE html>
<html lang="en">
<head>
<meta charset="utf-8">
<title>Velvet Brass Parade – Business Card</title>
<link href="https://fonts.googleapis.com/css2?family=Satisfy&family=PT+Sans:wght@400&display=swap" rel="stylesheet">
<style>
  :root {
    --paper: #ffffff;
    --title-grey: #6f6f6f;
    --panel-top: #ffffff;
    --panel-bottom: #c9c9c9;
    --ink: #111111;
    --bar-blue: #1672ba;
    --field-white: #ffffff;
    --art-top: #f1e6c8;
    --art-bottom: #dfe6df;
  }
  * { margin: 0; padding: 0; box-sizing: border-box; }
  html, body {
    width: 721px;
    height: 1200px;
    overflow: hidden;
    background: var(--paper);
  }
  .card {
    position: relative;
    width: 721px;
    height: 1200px;
    background: var(--paper);
    font-family: "PT Sans", Arial, sans-serif;
  }
  .band-name {
    position: absolute;
    top: 82px;
    left: 0;
    width: 100%;
    text-align: center;
    font-family: "Satisfy", cursive;
    font-weight: 400;
    font-size: 56px;
    line-height: 1.2;
    color: var(--title-grey);
  }
  .panel {
    position: absolute;
    left: 38px;
    top: 271px;
    width: 636px;
    height: 880px;
    background: linear-gradient(to bottom, var(--panel-top) 0%, var(--panel-bottom) 100%);
  }
  .music-art {
    position: absolute;
    left: 182px;
    top: 191px;
    width: 285px;
    height: 354px;
    background: linear-gradient(to bottom, var(--art-top) 0%, var(--art-bottom) 100%);
  }
  .contact {
    position: absolute;
    left: 30px;
    color: var(--ink);
    font-size: 28px;
    line-height: 1;
    white-space: nowrap;
  }
  .contact--phone { top: 692px; }
  .contact--email { top: 735px; }
  .web-bar {
    position: absolute;
    left: 28px;
    top: 782px;
    width: 443px;
    height: 64px;
    background: var(--bar-blue);
    border-radius: 8px;
  }
  .web-field {
    position: absolute;
    left: 13px;
    top: 10px;
    width: 356px;
    height: 44px;
    background: var(--field-white);
    border-radius: 6px;
    box-shadow: inset 0 3px 4px rgba(0,0,0,0.35);
    display: flex;
    align-items: center;
    padding-left: 8px;
    font-size: 21px;
    color: var(--ink);
    white-space: nowrap;
    overflow: hidden;
  }
  .search-icon {
    position: absolute;
    right: 22px;
    top: 14px;
    width: 36px;
    height: 36px;
  }
</style>
</head>
<body>
  <main class="card">
    <h1 class="band-name">Velvet Brass Parade</h1>
    <section class="panel">
      <div class="music-art" role="img" aria-label="Illustration area: speech bubbles with musical notes above rising bubbles and a row of colourful pebbles"></div>
      <p class="contact contact--phone">Phone: 0438 216 903</p>
      <p class="contact contact--email">email: velvetbrassparade@mailbox-demo.net</p>
      <div class="web-bar">
        <div class="web-field">www.velvetbrassparade-demo.com</div>
        <svg class="search-icon" viewBox="0 0 36 36" aria-hidden="true">
          <circle cx="20" cy="14" r="9" fill="none" stroke="#ffffff" stroke-width="4"/>
          <line x1="13.5" y1="20.5" x2="5" y2="29" stroke="#ffffff" stroke-width="5" stroke-linecap="round"/>
        </svg>
      </div>
    </section>
  </main>
</body>
</html>
```